elegant beautiful Hang tag for a novelty makeup towel

It's a black hand towel in the shape of a little black dress. it is called VELVET EVENING WRAP, it is a SECRET KEEPER MAKEUP TOWEL. (doesn't show our makeup stains) Made in USA

Target Market(s)

ALL Women , Makeup artists, novelty THIS WILL BE IN THE HALVERSTEAD STORES AND PEMBERCROFT STORES.

Industry/Entity Type

Makeup

Contact Information for Business Card

I actually need a hang tag for a homemade handmade towel. I have a logo that I want on the tag and know what we want to say on it, on back needs to say "The essential to every girl's wardrobe. So when the little black dress comes off, our VELVET EVENING WRAP is there to help you wash your day away. Include website www.velveteveningwrap.com OH INCLUDE TM (trademark sign next to logo please. Also, in small print on back from the makers of THE ORIGINAL SECRET KEEPER MAKEUP TOWEL. handmade in USA. also SECRET KEEPER MAKEUP TOWEL IN big font on front under logo sign with light colored pink lips after 'SECRET KEEPER" but have no idea about fonts, graphics, placement or design. Want it classy, elegant, girly! COLORS LIGHT BEIGER BACKGROUND WITH BLACK WRITING/ DESIGNS

Font styles to use
Serif
Decorative
Script

Colors
fff3d1

Requirements
Must have
• Black cream girly , also state in big writing that it's a " secret keeper makeup towel" with a tiny light pink lip between the show and makeup. Include www.velveteveningwrap.com Brightfold Goods, LLC
Nice to have
• Perhaps an outline of a little black dress. A black scroll edge of some sort around card. Classy

```html
<!DOCTYPE html>
<html lang="en">
<head>
<meta charset="utf-8">
<meta name="format-detection" content="telephone=no,email=no,address=no">
<title>Velvet Evening Wrap – Cards</title>
<link href="https://fonts.googleapis.com/css2?family=Open+Sans:wght@300;400&display=swap" rel="stylesheet">
<style>
  :root {
    --page: #e9e4da;
    --cream: #f3efe3;
    --cream-edge: #e6e0cf;
    --ink: #1c1c1c;
    --ink-soft: #3a3a3a;
    --black-card: #050505;
    --pale-type: #d9d6cf;
    --fine-type: #a9a59d;
  }
  * { margin: 0; padding: 0; box-sizing: border-box; }
  html, body { width: 1200px; height: 780px; overflow: hidden; }
  body {
    background: var(--page);
    font-family: "Open Sans", Arial, sans-serif;
    display: flex;
    align-items: center;
    justify-content: center;
    gap: 60px;
  }
  .card {
    width: 525px;
    height: 300px;
    border-radius: 22px;
    position: relative;
    box-shadow: 0 6px 18px rgba(0,0,0,0.18);
  }
  .card-front {
    background: linear-gradient(135deg, #f6f3ea 0%, var(--cream) 60%, var(--cream-edge) 100%);
    color: var(--ink);
  }
  .brand {
    position: absolute;
    top: 48px;
    left: 0;
    width: 100%;
    text-align: center;
    font-weight: 300;
    font-size: 34px;
    letter-spacing: 3px;
    color: var(--ink);
    line-height: 1;
  }
  .brand sup { font-size: 11px; letter-spacing: 0; vertical-align: 18px; margin-left: 2px; }
  .tagline-row {
    position: absolute;
    top: 96px;
    left: 30px;
    right: 30px;
    display: flex;
    align-items: center;
    gap: 12px;
  }
  .rule {
    flex: 1;
    height: 1px;
    background: var(--ink-soft);
  }
  .tagline {
    font-size: 11px;
    font-weight: 400;
    letter-spacing: 1px;
    color: var(--ink-soft);
    white-space: nowrap;
  }
  .contact {
    position: absolute;
    top: 150px;
    left: 0;
    width: 100%;
    text-align: center;
  }
  .contact-name {
    font-size: 22px;
    font-weight: 300;
    letter-spacing: 1px;
    margin-bottom: 12px;
  }
  .contact-line {
    font-size: 13px;
    font-weight: 300;
    color: var(--ink-soft);
    line-height: 21px;
  }
  .card-back {
    background: var(--black-card);
    color: var(--pale-type);
    display: flex;
    flex-direction: column;
    align-items: center;
    justify-content: center;
    text-align: center;
    padding: 0 44px;
  }
  .back-message {
    font-size: 15px;
    font-weight: 300;
    line-height: 24px;
    color: var(--pale-type);
    margin-bottom: 16px;
  }
  .back-website {
    font-size: 13px;
    font-weight: 300;
    letter-spacing: 0.3px;
    color: var(--pale-type);
    margin-bottom: 18px;
  }
  .back-fine {
    font-size: 10px;
    font-weight: 400;
    letter-spacing: 0.5px;
    line-height: 16px;
    color: var(--fine-type);
  }
</style>
</head>
<body>
  <section class="card card-front">
    <h1 class="brand">VELVET EVENING WRAP<sup>TM</sup></h1>
    <div class="tagline-row">
      <span class="rule"></span>
      <p class="tagline">SECRET KEEPER MAKEUP TOWEL</p>
      <span class="rule"></span>
    </div>
    <div class="contact">
      <p class="contact-name">MARA ELLIS</p>
      <p class="contact-line">555-014-2290</p>
      <p class="contact-line">mara@velveteveningwrap.com</p>
      <p class="contact-line">Post Office Box 2180, Alder Creek CA 90017</p>
    </div>
  </section>

  <section class="card card-back">
    <p class="back-message">The essential to every girl's wardrobe. So when the little black dress comes off, our VELVET EVENING WRAP is there to help you wash your day away.</p>
    <p class="back-website">www.velveteveningwrap.com</p>
    <p class="back-fine">From the makers of THE ORIGINAL SECRET KEEPER MAKEUP TOWEL</p>
    <p class="back-fine">Handmade in USA · Brightfold Goods, LLC</p>
  </section>
</body>
</html>
```